Business Card for my building company

I would like the card to make a statement, so as soon as you see the card you think "wow nice card' and then read the details on the card its self. Also i would like to be able to put in the detail for the MUST HAVES so please Crete a box that i can alter depending on who in my business needs the cards. Thank you

Target Market(s)

Any one looking to build a house/ townhouse or duplex

Industry/Entity Type

Home Builder

Contact Information for Business Card

I would like the card to have the logo on the card and the must haves

Font styles to use
Sans Serif

Requirements
Must have
• Name
• Phone Number
• Email Address
• Website
• Licence Number
• Abn

```html
<!DOCTYPE html>
<html lang="en">
<head>
<meta charset="utf-8">
<title>Broadland Builders – Business Card</title>
<link href="https://fonts.googleapis.com/css2?family=Open+Sans:wght@400;700;800&display=swap" rel="stylesheet">
<style>
  :root {
    --backdrop: #e9e6e1;
    --card: #ffffff;
    --ink: #111111;
    --text: #2a2a2a;
    --gold: #c9a24a;
    --muted: #555555;
  }
  html, body {
    margin: 0;
    width: 1200px;
    height: 1022px;
    overflow: hidden;
    background: var(--backdrop);
    font-family: "Open Sans", Arial, sans-serif;
  }
  .business-card {
    position: absolute;
    left: 150px;
    top: 254px;
    width: 900px;
    height: 514px;
    background: var(--card);
    border-radius: 22px;
    box-shadow: 0 14px 40px rgba(0,0,0,0.18);
    overflow: hidden;
  }
  .brand {
    position: absolute;
    left: 70px;
    bottom: 90px;
    width: 320px;
  }
  .brand-line {
    display: flex;
    align-items: flex-start;
    gap: 14px;
  }
  .brand-mark {
    flex: none;
    width: 34px;
    height: 34px;
    margin-top: 8px;
    background: var(--gold);
  }
  .brand-name {
    font-weight: 800;
    font-size: 40px;
    color: var(--ink);
    letter-spacing: 0.5px;
    text-transform: uppercase;
    line-height: 1.1;
  }
  .licence {
    margin-top: 12px;
    margin-left: 48px;
    font-size: 20px;
    color: var(--muted);
    letter-spacing: 1px;
  }
  .details {
    position: absolute;
    right: 60px;
    top: 70px;
    width: 380px;
  }
  .person-name {
    font-weight: 800;
    font-size: 38px;
    color: var(--ink);
    text-transform: uppercase;
    margin: 0;
    line-height: 1.1;
  }
  .person-role {
    font-size: 19px;
    color: var(--gold);
    text-transform: uppercase;
    letter-spacing: 1px;
    margin: 4px 0 14px;
  }
  .info-line {
    font-size: 20px;
    color: var(--text);
    margin: 0 0 8px;
  }
  .abn { margin-bottom: 22px; }
  .contact-list {
    list-style: none;
    padding: 0;
    margin: 0;
  }
  .contact-list li {
    display: flex;
    align-items: center;
    gap: 10px;
    font-size: 20px;
    color: var(--text);
    margin-bottom: 6px;
    white-space: nowrap;
  }
  .contact-list svg {
    width: 14px;
    height: 14px;
    flex: none;
  }
</style>
</head>
<body>
  <div class="business-card">
    <div class="brand">
      <div class="brand-line">
        <span class="brand-mark"></span>
        <span class="brand-name">Broadland<br>Builders</span>
      </div>
      <div class="licence">#LIC : 2409176</div>
    </div>

    <div class="details">
      <h1 class="person-name">Liam Porter</h1>
      <div class="person-role">Director</div>
      <p class="info-line">Harbourview QLD 4019</p>
      <p class="info-line abn">ABN : 61 204 889 310</p>
      <ul class="contact-list">
        <li>
          <svg viewBox="0 0 14 14" aria-hidden="true"><path d="M3 1 L5.5 1 L6.3 4 L4.8 5.2 C5.6 7 7 8.4 8.8 9.2 L10 7.7 L13 8.5 L13 11 C13 12 12 13 11 13 C5.5 13 1 8.5 1 3 C1 2 2 1 3 1 Z" fill="var(--gold)"/></svg>
          0400 123 456
        </li>
        <li>
          <svg viewBox="0 0 14 14" aria-hidden="true"><rect x="1" y="3" width="12" height="8.5" rx="1" fill="none" stroke="var(--gold)" stroke-width="1.6"/><path d="M1.5 3.5 L7 8 L12.5 3.5" fill="none" stroke="var(--gold)" stroke-width="1.6"/></svg>
          info@liamportermail.com
        </li>
        <li>
          <svg viewBox="0 0 14 14" aria-hidden="true"><circle cx="7" cy="7" r="5.8" fill="none" stroke="var(--gold)" stroke-width="1.5"/><ellipse cx="7" cy="7" rx="2.4" ry="5.8" fill="none" stroke="var(--gold)" stroke-width="1.2"/><line x1="1.2" y1="7" x2="12.8" y2="7" stroke="var(--gold)" stroke-width="1.2"/></svg>
          www.broadlandbuilders.com
        </li>
      </ul>
    </div>
  </div>
</body>
</html>
```